WP website design Harrow-Pelling(Contest)

We need a wordpress design that will incorporate a professional color scheme with company logo in a clean layout. The design needs to consider that this will be developed on a responsive theme. Colors are blue and green of the logo and and an accent color (perhaps very light brown/tan). Client wants a 'modern' look.

Industry/Entity Type

It Company

Font styles to use
Serif
Sans Serif

Colors

Designer to choose colors to be used in the design.

Requirements
Must have
• navigation: 1) Home; 2) Services; 3) Auctions by Type; 4) About Us; 5) QTV Digest 6) Videos; 7) Contact Us

VERY general idea of layout is attached, Site will have slideshow, image is attached. Widgets used to are: 1) Email Contact Form; 2) social media icons, FB LinedIn, YouTube; 3) Featured Auctions; 4) News & Events blog; Featured Video

Footer will have affiliation logos, contact info and perhaps smaller company logo:
Phone: (512) 555-0147 / Mobile: (512) 555-0183 (Mirel)
Email: mpelling417@mailvex.com / derek@harrowpelling.com
Address: 417 Bexley Rd • #F208 • PMB530 • Austin, TX 78790

Nice to have
• Use of a dropdown menu

```html
<!DOCTYPE html>
<html lang="en">
<head>
<meta charset="utf-8">
<title>Harrow-Pelling Auction Marketing</title>
<link href="https://fonts.googleapis.com/css2?family=Cabin:wght@400;500;600;700&family=Arimo:wght@400;700&display=swap" rel="stylesheet">
<style>
  :root{
    --brand-blue:#0f64a0;
    --brand-blue-dark:#0b4f82;
    --brand-green:#148a5c;
    --brand-green-dark:#0e7a4f;
    --ink:#1e1e1e;
    --muted:#3b3b3b;
    --rule:#cfcfcf;
    --footer:#2a2a2a;
    --white:#ffffff;
  }
  *{margin:0;padding:0;box-sizing:border-box}
  html,body{width:1045px;height:1200px;overflow:hidden;background:var(--white)}
  body{position:relative;font-family:"Cabin",sans-serif;color:var(--ink)}
  .abs{position:absolute}

  .site-header{left:0;top:0;width:1045px;height:131px;background:linear-gradient(#ffffff,#e6e6e6);border-bottom:3px solid var(--brand-green)}
  .brand{left:89px;top:10px;width:198px;height:107px;background:linear-gradient(#f6f6f6,#ececec);display:flex;flex-direction:column;align-items:center;justify-content:center;text-align:center}
  .brand-parent{font-size:22px;font-weight:700;color:var(--brand-blue);line-height:1.1}
  .brand-name{font-size:17px;font-weight:700;color:var(--brand-blue);line-height:1.15;margin-top:6px}
  .follow{left:611px;top:35px;font-size:16px;color:#333}
  .social{top:64px;width:28px;height:28px;border-radius:50%}
  .call{left:773px;top:39px;font-size:16px;color:var(--brand-blue)}
  .call b{color:var(--brand-green);font-weight:600;margin-right:6px}
  .mail{left:773px;top:67px;font-size:16px;color:var(--brand-blue)}

  .main-nav{left:0;top:134px;width:1045px;height:32px;background:var(--white)}
  .nav-item{top:9px;font-family:"Arimo",sans-serif;font-size:12px;font-weight:700;color:#222;letter-spacing:.2px}
  .nav-sep{top:5px;width:1px;height:22px;background:var(--rule)}
  .nav-mark{left:116px;top:0;width:0;height:0;border-left:5px solid transparent;border-right:5px solid transparent;border-top:5px solid var(--brand-green)}

  .hero{left:0;top:166px;width:1045px;height:406px;background:var(--brand-blue)}
  .slide{left:87px;top:25px;width:871px;height:355px;background:var(--white);padding:4px}
  .slide-photo{width:100%;height:100%;position:relative;background:linear-gradient(180deg,#3d6a33 0%,#7a8a7a 35%,#8a4a3a 60%,#4a5a3a 100%)}
  .slide-caption{left:0;bottom:0;width:100%;height:67px;background:rgba(40,40,40,.72)}
  .slide-title{left:19px;top:16px;font-size:24px;font-weight:600;color:var(--white)}
  .btn-light{left:702px;top:11px;width:136px;height:35px;border-radius:3px;background:linear-gradient(#ffffff,#d8d8d8);font-size:19px;font-weight:500;color:#333;display:flex;align-items:center;justify-content:center}

  .intro{left:0;top:600px;width:1045px;text-align:center;font-size:17.5px;line-height:28px;color:#222}

  .features{left:0;top:704px;width:1045px;height:370px;background:linear-gradient(var(--brand-green),var(--brand-green-dark))}
  .upcoming{left:87px;top:0;width:301px;height:370px;background:var(--white);border:1px solid #bbb;border-bottom:none}
  .upcoming h2{position:absolute;left:19px;top:11px;font-size:22px;font-weight:500;color:var(--brand-blue);letter-spacing:.5px}
  .upcoming-photo{left:20px;top:62px;width:255px;height:111px;border:2px solid var(--brand-blue);background:linear-gradient(#9aa8a6,#3f7a62 60%,#c9cfcf)}
  .upcoming p{position:absolute;left:21px;top:196px;width:260px;font-family:"Arimo",sans-serif;font-size:11.3px;line-height:17.4px;color:#222}
  .btn-blue{left:21px;top:299px;width:106px;height:27px;border-radius:2px;background:linear-gradient(#1a70ad,var(--brand-blue-dark));color:var(--white);font-size:15px;font-weight:500;display:flex;align-items:center;justify-content:center}
  .tile-title{font-size:16px;font-weight:600;color:var(--white);letter-spacing:1px}
  .tile-photo{width:203px;height:108px;border:3px solid var(--white);box-shadow:0 1px 3px rgba(0,0,0,.3)}

  .site-footer{left:0;top:1074px;width:1045px;height:126px;background:var(--footer)}
  .footer-info{left:87px;top:22px;font-family:"Arimo",sans-serif;font-size:11.3px;line-height:20.8px;color:var(--white)}
  .badge{background:#8a8a8a}
</style>
</head>
<body>

<header class="site-header abs">
  <div class="brand abs">
    <span class="brand-parent">Allied Acreage</span>
    <span class="brand-name">Harrow Pelling<br>Auction Marketing</span>
  </div>
  <div class="follow abs">Follow us on</div>
  <span class="social abs" style="left:610px;background:var(--brand-blue-dark)" aria-label="Social profile 1"></span>
  <span class="social abs" style="left:646px;background:var(--brand-blue)" aria-label="Social profile 2"></span>
  <span class="social abs" style="left:683px;background:var(--brand-green)" aria-label="Social profile 3"></span>
  <span class="social abs" style="left:718px;background:var(--brand-green-dark)" aria-label="Social profile 4"></span>
  <div class="call abs"><b>Call Us:</b>1800 555 0192</div>
  <div class="mail abs">info@harrowpelling.com</div>
</header>

<nav class="main-nav abs">
  <span class="nav-mark abs"></span>
  <span class="nav-item abs" style="left:105px">HOME</span>
  <span class="nav-sep abs" style="left:165px"></span>
  <span class="nav-item abs" style="left:192px">SERVICES</span>
  <span class="nav-sep abs" style="left:275px"></span>
  <span class="nav-item abs" style="left:301px">AUCTIONS BY TYPE</span>
  <span class="nav-sep abs" style="left:437px"></span>
  <span class="nav-item abs" style="left:466px">ABOUT US</span>
  <span class="nav-sep abs" style="left:550px"></span>
  <span class="nav-item abs" style="left:577px">QTV DIGEST</span>
  <span class="nav-sep abs" style="left:678px"></span>
  <span class="nav-item abs" style="left:706px">VIDEOS</span>
  <span class="nav-sep abs" style="left:774px"></span>
  <span class="nav-item abs" style="left:801px">CONTACT US</span>
</nav>

<section class="hero abs">
  <div class="slide abs">
    <div class="slide-photo" role="img" aria-label="Photo of a red brick two-storey house with grey roof among trees">
      <div class="slide-caption abs">
        <span class="slide-title abs">Making "SOLD" Our Specialty for 30 Years</span>
        <span class="btn-light abs">Read More</span>
      </div>
    </div>
  </div>
</section>

<p class="intro abs">The go-to business asset liquidation and real estate at auction solution provider in Texas and<br>across the southwest for over 30 years using our proprietary QTV process.</p>

<section class="features abs">
  <article class="upcoming abs">
    <h2>UPCOMING AUCTION</h2>
    <div class="upcoming-photo abs" role="img" aria-label="Photo of a machine shop floor with green industrial lathes"></div>
    <p>Lorem ipsum dolor sit amet, consectetur adipiscing elit, sed do eiusmod tempor incid-idunt ut labore et dolore magna aliqua. repre-henderit in voluptate velit esse cillum dolore eu fugiat nulla pariatur.</p>
    <span class="btn-blue abs">Read More</span>
  </article>

  <span class="tile-title abs" style="left:475px;top:27px">REAL ESTATE</span>
  <div class="tile-photo abs" style="left:473px;top:57px;background:linear-gradient(#8fb4de,#8a7f5e 55%,#6f6a4e)" role="img" aria-label="Photo of a suburban house with brown gables"></div>
  <span class="tile-title abs" style="left:714px;top:27px">BUSINESS LIQUIDATION</span>
  <div class="tile-photo abs" style="left:714px;top:57px;background:linear-gradient(#2f7fd0,#c9c9c4 55%,#7a8a6a)" role="img" aria-label="Photo of a two-storey white house under a blue sky"></div>
  <span class="tile-title abs" style="left:475px;top:201px">COMMERCIAL ASSETS</span>
  <div class="tile-photo abs" style="left:473px;top:231px;background:linear-gradient(#b8cce0,#b89f82 50%,#8a7a66)" role="img" aria-label="Photo of a stone and stucco family home"></div>
  <span class="tile-title abs" style="left:718px;top:199px">APPRAISALS</span>
  <div class="tile-photo abs" style="left:714px;top:231px;background:linear-gradient(#a9c4dd,#c9c6bf 50%,#8e8a86)" role="img" aria-label="Photo of a grey sided house with white trim"></div>
</section>

<footer class="site-footer abs">
  <div class="footer-info abs">
    The QTV Digest: Derek Pelling Receives Lifetime Achievement Award Llinks to QTV Digest (former news)<br>
    Phone: (512) 555-0147 / Mobile: (512) 555-0183 (Mirel)<br>
    Email: mpelling417@mailvex.com / derek@harrowpelling.com<br>
    Address: 417 Bexley Rd • #F208 • PMB530 • Austin, TX 78790
  </div>
  <span class="badge abs" style="left:784px;top:16px;width:46px;height:46px;border-radius:50%" aria-label="Affiliation badge"></span>
  <span class="badge abs" style="left:851px;top:16px;width:42px;height:44px" aria-label="Affiliation badge"></span>
  <span class="badge abs" style="left:771px;top:68px;width:52px;height:42px" aria-label="Certification badge"></span>
  <span class="badge abs" style="left:831px;top:72px;width:94px;height:34px" aria-label="Certification badge"></span>
</footer>

</body>
</html>
```